Kitchen and bathroom exhaust fan cleaning business card design

A new business cleaning domestic - not commercial - exhaust/extractor fans in kitchens, bathrooms and en suites and kitchen range hood filters.

We would like a bright colour suggesting cleanliness (such a syellow or light green?)

I would like to see on the card preferably on the reverse:

"We clean kitchen and bathroom exhaust fans & Vormo Heatlites
and
clean and repair range hood filters and replace carbon filters

We give Pensioner discounts

Designers pls note the TM in the contact filed after Brisko Airworks should be superscript as in the trademark sign. On the reverse of the card, I would like:: "We clean kitchen and bathroom exhaust fans & Vormo Heatlites & clean and repair range hood filters and replace carbon filters We give Pensioner discounts

Reason: I will be out of the country for several days

Target Market(s)

people who are too lazy or too busy to clean their fan units and pensioners and others who are unable to do it.

Industry/Entity Type

Business

Contact Information for Business Card

Brisko AirworksTM Designer pls note the TM should be superscript as in the trademark sign
Alan Petworth
Mob: 0491 570 263
Email: briskoairworks@postlume.net
PO Box 7152, Hawker ACT 2614

Requirements
Must have
• Designer pls note the TM in the contact filed after Brisko Airworks should be superscript as in the trademark sign.

On the reverse

and

```html
<!DOCTYPE html>
<html lang="en">
<head>
<meta charset="utf-8">
<title>Brisko Airworks – Business Card</title>
<link rel="stylesheet" href="https://fonts.googleapis.com/css2?family=Ubuntu:wght@400;500&display=swap">
<style>
  :root {
    --card-yellow: #ffff00;
    --band-green: #2fe51a;
    --ink: #1a1a1a;
    --band-text: #e9ffe3;
    --backdrop: #e9e9e6;
    --fan-grey: #d4d6d8;
    --lamp-grey: #c9cbcd;
  }
  * { box-sizing: border-box; margin: 0; padding: 0; }
  html, body {
    width: 1200px; height: 865px; overflow: hidden;
    background: var(--backdrop);
    font-family: "Ubuntu", Arial, sans-serif;
    color: var(--ink);
  }
  .sheet {
    position: relative; width: 1200px; height: 865px;
    display: flex; justify-content: center; align-items: center; gap: 60px;
  }
  .card {
    position: relative; width: 520px; height: 318px;
    background: var(--card-yellow);
    overflow: hidden;
    box-shadow: 0 4px 14px rgba(0,0,0,.18);
  }
  .brand {
    position: absolute; font-size: 24px; font-weight: 500;
    letter-spacing: -0.5px; text-transform: uppercase; white-space: nowrap;
  }
  .brand sup {
    display: inline-block; font-size: 8px; font-weight: 500;
    width: 20px; height: 20px; line-height: 17px; text-align: center;
    border: 1.5px solid var(--ink); border-radius: 50%;
    vertical-align: super; margin-left: 8px; letter-spacing: 0;
  }
  /* front */
  .front .tab { position: absolute; left: 150px; top: 24px; width: 70px; height: 38px; background: var(--band-green); }
  .front .brand { left: 190px; top: 52px; }
  .front .fan-photo {
    position: absolute; left: 36px; top: 26px; width: 112px; height: 112px; border-radius: 50%;
    background: radial-gradient(circle, #f4f5f6 0%, var(--fan-grey) 100%);
  }
  .front .lamp-photo {
    position: absolute; left: 48px; top: 156px; width: 90px; height: 90px; border-radius: 10px;
    background: radial-gradient(circle, #eceeef 0%, var(--lamp-grey) 100%);
  }
  .front .name-band { position: absolute; right: 0; top: 146px; width: 210px; height: 36px; background: var(--band-green); }
  .front .person { position: absolute; left: 290px; top: 192px; }
  .front .person-name { font-size: 27px; font-weight: 500; }
  .front .phone { font-size: 19px; margin-top: 4px; display: flex; align-items: center; gap: 6px; }
  .front .postal { position: absolute; left: 150px; top: 258px; font-size: 16px; line-height: 24px; }
  /* back */
  .back .brand { left: 86px; top: 34px; }
  .back .services { position: absolute; left: 86px; top: 80px; list-style: none; font-size: 15px; line-height: 22px; }
  .back .services li { display: flex; align-items: center; gap: 10px; }
  .back .services li::before {
    content: ""; width: 0; height: 0;
    border-left: 7px solid var(--ink); border-top: 4px solid transparent; border-bottom: 4px solid transparent;
  }
  .back .promise-band { position: absolute; left: 0; top: 218px; width: 470px; height: 36px; }
  .back .promise {
    position: absolute; left: 30px; top: 226px; font-size: 15px; color: var(--band-text); white-space: nowrap;
  }
</style>
</head>
<body>
<main class="sheet">
  <section class="card front" aria-label="Card front">
    <div class="tab"></div>
    <div class="fan-photo" role="img" aria-label="Photo of a round bathroom exhaust fan"></div>
    <div class="lamp-photo" role="img" aria-label="Photo of a four-lamp bathroom heat light unit"></div>
    <h1 class="brand">Brisko Airworks<sup>TM</sup></h1>
    <div class="name-band"></div>
    <div class="person">
      <p class="person-name">Alan Petworth</p>
      <p class="phone">
        <svg width="14" height="16" viewBox="0 0 14 16" aria-hidden="true"><path d="M3 1 L6 4 L4.5 6 Q6 10 9 11.5 L11 10 L13.5 13 L11.5 15 Q3 13 1 3 Z" fill="#1a1a1a"/></svg>
        0491 570 263
      </p>
    </div>
    <address class="postal" style="font-style:normal">
      PO Box 7152, Hawker ACT 2614<br>
      Email: briskoairworks@postlume.net
    </address>
  </section>

  <section class="card back" aria-label="Card back">
    <h2 class="brand">Brisko Airworks<sup>TM</sup></h2>
    <ul class="services">
      <li>Clean Kitchen, Bathroom &amp; en suite Exhaust Fans</li>
      <li>Clean range hood filters offsite</li>
      <li>Replace old charcoal filters</li>
      <li>Repair range hood filters.</li>
      <li>Clean anything else you want.</li>
    </ul>
    <svg class="promise-band" viewBox="0 0 470 36" aria-hidden="true"><polygon points="0,0 440,0 470,36 0,36" fill="#2fe51a"/></svg>
    <p class="promise">We are fully insured and give Pensioner Discounts</p>
  </section>
</main>
</body>
</html>
```